Alcohol designs Birthday Sign's needs more templates

We are after 10 new designs for signable custom birthday signs, alcohol theme inspired (beer, wine, spirits) for this batch, You do not need to provide 10 designs however the winner will be based on final look and quantity.
For example someone may win with one design or ten designs. We will also look at purchasing more individual designs for any winners or potential winners. Designs must be in layers, CMYK, 8bits channel, saved as TIFF or PDS or AI, size is 460mm wide x by 1060mm high with 30mm bleed included, total graphic size will be 430 x 1030 at 300ppi, any text must be editable and font files included. see attached for sample's, signable area needs to be on each design and a sample persons name, other then that we a excited to see what everyone comes up with
Updates
Reason: Allow more designs to be supplied form current designers and new designers. Also to allow us to choose more than one designer by adding a second/third place
Target Market(s)
Birthday
Requirements
Must have
- Layers.
- Space for people to sign
Nice to have
- At least 3 designs (These can be of the same template you design just with a small them change beer, wine etc)

```html
<!DOCTYPE html>
<html lang="en">
<head>
<meta charset="utf-8">
<title>Birthday Can Sign</title>
<link href="https://fonts.googleapis.com/css2?family=Anton&family=Yellowtail&family=Roboto:wght@700;900&display=swap" rel="stylesheet">
<style>
  :root {
    --copper-dark: #b4561c;
    --copper-mid: #e2832a;
    --copper-light: #f8a53a;
    --silver-light: #f4f4f4;
    --silver-mid: #d2d3d5;
    --silver-dark: #a9abae;
    --label-rim: #e9eaeb;
    --blue-dark: #16559e;
    --blue-light: #2f7cd0;
    --badge-grey: #8d9094;
    --ink: #111111;
    --white: #ffffff;
  }
  html, body {
    margin: 0;
    padding: 0;
    width: 1200px;
    height: 2764px;
    overflow: hidden;
    background: #ffffff;
  }
  .sign {
    display: block;
    width: 1200px;
    height: 2764px;
  }
  .age-number {
    font-family: "Roboto", Arial, sans-serif;
    font-weight: 900;
    font-size: 104px;
    fill: var(--ink);
  }
  .greeting-happy {
    font-family: "Anton", Impact, sans-serif;
    font-size: 190px;
    fill: var(--ink);
    letter-spacing: 2px;
  }
  .greeting-birthday {
    font-family: "Roboto", Arial, sans-serif;
    font-weight: 900;
    font-size: 76px;
    fill: var(--ink);
  }
  .guest-name {
    font-family: "Yellowtail", cursive;
    font-size: 190px;
    fill: var(--white);
  }
  .tagline-main {
    font-family: "Roboto", Arial, sans-serif;
    font-weight: 900;
    font-size: 62px;
    fill: var(--blue-dark);
    letter-spacing: 2px;
  }
  .tagline-sub {
    font-family: "Roboto", Arial, sans-serif;
    font-weight: 700;
    font-size: 46px;
    fill: var(--blue-dark);
    letter-spacing: 3px;
  }
</style>
</head>
<body>
<svg class="sign" viewBox="0 0 1200 2764" xmlns="http://www.w3.org/2000/svg">
  <defs>
    <linearGradient id="can-body" x1="0" y1="0" x2="1" y2="0">
      <stop offset="0" stop-color="var(--copper-dark)"/>
      <stop offset="0.3" stop-color="var(--copper-mid)"/>
      <stop offset="0.5" stop-color="var(--copper-light)"/>
      <stop offset="0.7" stop-color="var(--copper-mid)"/>
      <stop offset="1" stop-color="var(--copper-dark)"/>
    </linearGradient>
    <linearGradient id="silver" x1="0" y1="0" x2="1" y2="0">
      <stop offset="0" stop-color="var(--silver-dark)"/>
      <stop offset="0.35" stop-color="var(--silver-mid)"/>
      <stop offset="0.5" stop-color="var(--silver-light)"/>
      <stop offset="0.65" stop-color="var(--silver-mid)"/>
      <stop offset="1" stop-color="var(--silver-dark)"/>
    </linearGradient>
    <linearGradient id="blue-band" x1="0" y1="0" x2="1" y2="0">
      <stop offset="0" stop-color="var(--blue-dark)"/>
      <stop offset="0.5" stop-color="var(--blue-light)"/>
      <stop offset="1" stop-color="var(--blue-dark)"/>
    </linearGradient>
    <radialGradient id="badge-fill" cx="0.5" cy="0.5" r="0.5">
      <stop offset="0" stop-color="#ffffff"/>
      <stop offset="0.7" stop-color="#d9dadc"/>
      <stop offset="1" stop-color="var(--badge-grey)"/>
    </radialGradient>
  </defs>

  <!-- can body -->
  <rect class="can-body" x="0" y="0" width="1200" height="2764" fill="url(#can-body)"/>

  <!-- top collar band -->
  <g class="top-collar">
    <rect x="0" y="120" width="1200" height="268" fill="url(#silver)"/>
    <polygon points="0,300 1200,150 1200,232 0,388" fill="url(#blue-band)"/>
    <circle cx="600" cy="190" r="90" fill="url(#badge-fill)" stroke="var(--white)" stroke-width="6"
            role="img" aria-label="Round badge with a small city skyline pattern"/>
    <text class="age-number" x="600" y="226" text-anchor="middle">32</text>
  </g>

  <!-- main label -->
  <g class="main-label">
    <path d="M168,1340 Q168,1220 330,1150 Q600,1040 870,1150 Q1032,1220 1032,1340
             L1032,2330 Q1032,2430 930,2510 Q880,2620 600,2620 Q320,2620 270,2510 Q168,2430 168,2330 Z"
          fill="url(#silver)" stroke="var(--label-rim)" stroke-width="14"/>

    <circle cx="600" cy="1520" r="232" fill="url(#badge-fill)" stroke="var(--white)" stroke-width="8"
            role="img" aria-label="Round badge with a city skyline seen from below"/>
    <text class="greeting-happy" x="600" y="1580" text-anchor="middle">HAPPY</text>
    <text class="greeting-birthday" x="600" y="1660" text-anchor="middle">BIRTHDAY</text>

    <polygon class="name-band" points="150,1770 1050,1720 1050,2010 150,2060" fill="url(#blue-band)"/>
    <text class="guest-name" x="600" y="1955" text-anchor="middle" transform="rotate(-3 600 1900)">Sam Porter</text>

    <text class="tagline-main" x="600" y="2315" text-anchor="middle">PREMIUM</text>
    <text class="tagline-sub" x="600" y="2390" text-anchor="middle">PARTY</text>
  </g>
</svg>
</body>
</html>
```